A3 Poster Design for BUSINESS COACHING services

A3 Poster design for business coaching - we want it to be visual - minimal words. Needs to contain:
- our logo (uploaded)
- the words BUSINESS COACHING - Business or a Hobby? Talk to us today about our business coaching services to take your business to the next level
- and some graphics (open to ideas of something representative of coaching/working together/ improving business profits/success)
The poster will be physically in our business premises and will be more a cue for existing clients to ask us about a service they may not know we offer and so why it doesn't need to be informational

Target Market(s)

Small to Medium Business Owners

Industry/Entity Type

Small Business

Requirements
Must have
• Needs to contain:
• - our logo (uploaded)
• - the words BUSINESS COACHING - Business or a Hobby? Talk to us today about our business coaching services to take your business to the next level
• - and some graphics (open to ideas of something representative of coaching/working together/ improving business profits/success)

```html
<!DOCTYPE html>
<html lang="en">
<head>
<meta charset="utf-8">
<title>Business or a Hobby? – Business Coaching Poster</title>
<link rel="stylesheet" href="https://fonts.googleapis.com/css2?family=Montserrat:wght@700;800&family=Itim&display=swap">
<style>
  :root {
    --page-bg: #e6e6e6;
    --poster-light: #f1f1f2;
    --poster-mid: #d9dadc;
    --poster-edge: #c4c5c7;
    --brand-green: #6b8e23;
    --headline-text: #ebebeb;
    --arrow-red: #c61f27;
    --arrow-shade: #9e1820;
    --rule-dark: #555759;
    --footer-bg: #ececec;
    --ink: #222222;
    --scooter-yellow: #e8b923;
    --suit-grey: #5a5a5a;
  }
  * { margin: 0; padding: 0; box-sizing: border-box; }
  html, body {
    width: 1200px;
    height: 960px;
    overflow: hidden;
    background: var(--page-bg);
  }
  .canvas {
    position: relative;
    width: 1200px;
    height: 960px;
  }
  .poster {
    position: absolute;
    left: 270px;
    top: 20px;
    width: 702px;
    height: 980px;
    transform: scale(0.9388);
    transform-origin: top left;
    overflow: hidden;
    background: radial-gradient(ellipse at 55% 45%, var(--poster-light) 0%, var(--poster-mid) 60%, var(--poster-edge) 100%);
  }
  .headline-band {
    position: absolute;
    left: 4px;
    height: 62px;
    background: var(--brand-green);
    color: var(--headline-text);
    font-family: "Montserrat", sans-serif;
    font-weight: 800;
    font-size: 47px;
    letter-spacing: 4px;
    line-height: 62px;
    padding-left: 14px;
    white-space: nowrap;
  }
  .headline-band--top { top: 55px; width: 348px; }
  .headline-band--bottom { top: 135px; width: 450px; }
  .rider-illustration {
    position: absolute;
    left: 140px;
    top: 228px;
    width: 320px;
    height: 225px;
    border-radius: 12px;
    background: linear-gradient(160deg, var(--suit-grey) 0%, #8a8a8a 40%, var(--scooter-yellow) 100%);
  }
  .growth-chart {
    position: absolute;
    left: 0;
    top: 0;
    width: 702px;
    height: 980px;
  }
  .footer {
    position: absolute;
    left: 0;
    top: 831px;
    width: 702px;
    height: 144px;
    background: var(--footer-bg);
  }
  .footer__message {
    position: absolute;
    left: 37px;
    top: 44px;
    font-family: "Itim", sans-serif;
    font-size: 19px;
    letter-spacing: 1.6px;
    line-height: 38px;
    color: var(--ink);
  }
  .footer__divider {
    position: absolute;
    left: 519px;
    top: 26px;
    width: 2px;
    height: 94px;
    background: var(--ink);
  }
  .footer__brand {
    position: absolute;
    left: 530px;
    top: 30px;
    width: 150px;
    text-align: center;
  }
  .footer__brand-mark {
    display: block;
    width: 30px;
    height: 30px;
    margin: 0 auto 8px;
    border-radius: 50%;
    background: var(--brand-green);
  }
  .footer__brand-name {
    font-family: "Montserrat", sans-serif;
    font-weight: 700;
    font-size: 16px;
    line-height: 19px;
    color: var(--rule-dark);
  }
  .footer__accent {
    position: absolute;
    left: 0;
    top: 975px;
    width: 702px;
    height: 5px;
    background: var(--brand-green);
  }
</style>
</head>
<body>
<main class="canvas">
  <section class="poster" aria-label="Business coaching poster">
    <h1>
      <span class="headline-band headline-band--top">BUSINESS</span>
      <span class="headline-band headline-band--bottom">OR A HOBBY?</span>
    </h1>

    <div class="rider-illustration" role="img"
      aria-label="Cartoon businessman riding a yellow scooter up the growth arrow, briefcase flying behind him"></div>

    <svg class="growth-chart" viewBox="0 0 702 980" aria-hidden="true">
      <polygon fill="var(--arrow-red)"
        points="0,675 138,588 215,653 360,507 390,545 470,465 468,435 580,400 557,550 525,520 398,633 360,597 222,740 138,680 0,770"/>
      <polygon fill="var(--arrow-shade)"
        points="0,675 138,588 215,653 360,507 390,545 470,465 470,487 390,567 360,529 215,675 138,610 0,697"/>
      <rect x="0" y="825" width="702" height="6" fill="var(--rule-dark)"/>
      <polygon fill="var(--footer-bg)" points="124,831 146,801 146,831"/>
    </svg>

    <footer class="footer">
      <p class="footer__message">Talk to us today about our business coaching<br>services to take your business to the next level.</p>
      <div class="footer__divider"></div>
      <div class="footer__brand">
        <span class="footer__brand-mark"></span>
        <p class="footer__brand-name">Brightpath Advisory</p>
      </div>
    </footer>
    <div class="footer__accent"></div>
  </section>
</main>
</body>
</html>
```